App to track miniature golf scores and provides clues to puzzles (Pemberly Under Glass)

A mini-golf scorecard, selfies, badges, rules and clues. See attached for details. The coding and deployment will be provided by someone else, but those requirements are also listed in doc. We need to be able to update any text fields after design is handed over. This app is only for ios.

Target Market(s)

Families

Industry/Entity Type

Entertainment

Requirements
Must have
• The pages listed in the document is needed. Colors are also provided.
Nice to have
• Small animation effects
Should not have
• dark or psychedelic

```html
<!DOCTYPE html>
<html lang="en">
<head>
<meta charset="utf-8">
<title>Pemberly Under Glass – Mini Golf App Screens</title>
<link href="https://fonts.googleapis.com/css2?family=Jost:wght@400;500;600;700&display=swap" rel="stylesheet">
<style>
:root{
  --green:#1fd07a;
  --green-dark:#14b566;
  --green-soft:#e6f9ef;
  --ink:#1d1d1f;
  --muted:#7a7f85;
  --line:#d9dde0;
  --brand:#e2655c;
  --pink:#ec5a7c;
  --paper:#ffffff;
  --photo-a:#c8b39a;
  --photo-b:#6f6a66;
}
*{box-sizing:border-box;margin:0;padding:0}
html,body{width:1200px;height:4196px;overflow:hidden;background:var(--paper)}
body{position:relative;font-family:"Jost",Arial,sans-serif;color:var(--ink)}
.phone{position:absolute;width:322px;height:512px;border:5px solid var(--green);border-radius:32px;background:var(--paper);overflow:hidden}
.notch{position:absolute;top:0;left:50%;width:120px;height:15px;margin-left:-60px;background:var(--green);border-radius:0 0 12px 12px}
.status{position:absolute;top:6px;left:22px;font-size:8px;font-weight:600}
.caption{position:absolute;width:322px;text-align:center;font-size:17px;font-weight:700;letter-spacing:1px;text-transform:uppercase}
.screen{position:absolute;top:34px;left:18px;right:18px;bottom:0}
.topbar{display:flex;align-items:center;gap:10px;height:22px;margin-bottom:12px}
.back{font-size:14px;line-height:1;color:var(--ink)}
.title{font-size:11px;font-weight:700;letter-spacing:.5px;text-transform:uppercase}
.brand{font-size:12px;font-weight:700;color:var(--brand);text-align:center;letter-spacing:.5px;text-transform:uppercase}
.brand-small{position:absolute;bottom:18px;left:0;right:0;font-size:9px;font-weight:700;text-align:center;letter-spacing:1px;text-transform:uppercase}
.btn{position:absolute;left:50%;width:130px;height:28px;margin-left:-65px;background:var(--green);color:#fff;font-size:9px;font-weight:700;letter-spacing:1px;text-transform:uppercase;display:flex;align-items:center;justify-content:center;border-radius:2px}
.btn.bottom{bottom:22px}
.note{font-size:8px;color:var(--muted);text-align:center;line-height:1.4}
.card{background:var(--green);color:#fff;border-radius:3px;display:flex;align-items:center;gap:10px;padding:9px 10px;margin-bottom:8px;min-height:50px}
.card .num{font-size:17px;font-weight:700}
.card .txt{font-size:9px;line-height:1.35;font-weight:500}
.card .more{display:block;text-align:center;font-size:6px;opacity:.85;margin-top:2px}
.badge-icon{flex:none;width:24px;height:24px;border:1.5px solid #fff;border-radius:50%}
.code-row{display:flex;justify-content:center;gap:10px;margin-top:22px}
.code-box{width:32px;height:36px;border:2px solid var(--green);border-radius:3px}
.input{font-size:9px;color:var(--muted);border-bottom:1px solid var(--line);padding:8px 0;margin-bottom:8px}
.label{font-size:8px;font-weight:600;margin:10px 0 8px}
.count-row{display:flex;justify-content:center;gap:8px;margin-bottom:12px}
.count{width:28px;height:24px;border:1.5px solid var(--green);font-size:8px;font-weight:600;display:flex;align-items:center;justify-content:center;color:var(--green-dark)}
.count.on{background:var(--green);color:#fff}
.hole-grid{display:grid;grid-template-columns:repeat(3,1fr);gap:8px;margin-top:22px}
.hole{background:var(--green);color:#fff;height:54px;display:flex;flex-direction:column;align-items:center;justify-content:center;font-weight:700;font-size:10px;line-height:1.2;letter-spacing:.5px}
.hole-bar{display:flex;justify-content:space-between;margin-top:10px}
.chip{background:var(--green);color:#fff;font-weight:700;font-size:10px;padding:5px 10px;letter-spacing:.5px}
.icon-pair{display:flex;justify-content:center;gap:18px;margin:14px 0}
.player{margin-top:10px;position:relative;height:40px}
.player .name{font-size:8px;font-weight:600}
.player .score{font-size:7px;color:var(--muted);margin-top:10px}
.player .current{position:absolute;right:0;top:22px;font-size:7px;color:var(--muted)}
.slider{position:absolute;left:90px;right:0;top:10px;height:1px;background:var(--green)}
.knob{position:absolute;top:-4px;width:9px;height:9px;border-radius:50%;border:1.5px solid var(--green);background:#fff}
.knob-val{position:absolute;top:-14px;font-size:7px;color:var(--green-dark);font-weight:600}
.dock{position:absolute;bottom:22px;left:0;right:0;display:flex;justify-content:space-between;align-items:center}
.dock .square{width:28px;height:28px;background:var(--green);display:flex;align-items:center;justify-content:center;color:#fff;font-size:13px;font-weight:700}
.dock .submit{width:130px;height:28px;background:var(--green);color:#fff;font-size:9px;font-weight:700;letter-spacing:1px;display:flex;align-items:center;justify-content:center}
.menu{position:absolute;left:0;bottom:56px;width:150px;background:#fff;box-shadow:0 2px 10px rgba(0,0,0,.15);padding:6px 0}
.menu-item{display:flex;align-items:center;gap:8px;font-size:8px;padding:7px 10px}
.menu-item i{display:block;width:10px;height:10px;border:1.2px solid var(--green);border-radius:50%}
.clue{background:var(--green);color:#fff;text-align:center;padding:10px;margin-bottom:10px;border-radius:3px}
.clue b{display:block;font-size:13px;letter-spacing:.5px}
.clue span{font-size:8px}
.dim{position:absolute;inset:0;background:#f3f4f5}
.modal{position:absolute;left:30px;right:30px;top:170px;background:#fff;box-shadow:0 3px 14px rgba(0,0,0,.15);padding:20px 16px 50px;text-align:center}
.modal h3{font-size:11px;font-weight:700;margin-bottom:10px}
.modal .btn{bottom:14px;width:110px;margin-left:-55px}
.total{width:150px;height:150px;margin:34px auto 0;background:var(--green);color:#fff;text-align:center;display:flex;flex-direction:column;justify-content:center}
.total b{font-size:26px}
.total span{font-size:10px;font-weight:700;letter-spacing:1px}
.photo{background:linear-gradient(160deg,var(--photo-a),var(--photo-b))}
.camera{display:flex;justify-content:center;align-items:center;gap:40px;position:absolute;bottom:24px;left:0;right:0}
.shutter{width:34px;height:34px;border:2.5px solid var(--ink);border-radius:50%}
.cam-small{width:14px;height:14px;border:1.5px solid var(--ink);border-radius:4px}
.table{background:var(--green);color:#fff;padding:10px;margin-top:10px}
.table table{width:100%;border-collapse:collapse;font-size:7px}
.table td,.table th{padding:6px 2px;text-align:center;border-bottom:1px solid rgba(255,255,255,.35)}
.table th{font-weight:500}
.table td:first-child{text-align:left;font-weight:700}
.team{background:var(--green);color:#fff;display:flex;justify-content:space-between;font-size:8px;font-weight:700;padding:8px 10px;margin-bottom:6px}
</style>
</head>
<body>

<!-- Row 1 -->
<div class="phone" style="left:130px;top:78px">
  <div class="notch"></div><div class="status">9:41</div>
  <div class="screen">
    <div class="brand" style="margin-top:6px">Pemberly Under Glass</div>
    <div style="margin-top:92px;text-align:center;font-size:12px;font-weight:700">ENTER CODE TO PLAY</div>
    <div class="note" style="margin-top:8px">Please enter the code provided on your card.</div>
    <div class="code-row"><div class="code-box"></div><div class="code-box"></div><div class="code-box"></div><div class="code-box"></div></div>
    <div class="btn" style="top:332px">Continue</div>
    <div class="brand-small">Burrow Putt</div>
  </div>
</div>
<div class="caption" style="left:130px;top:624px">Login Screen</div>

<div class="phone" style="left:471px;top:78px">
  <div class="notch"></div><div class="status">9:41</div>
  <div class="screen">
    <div class="topbar"><span class="back">←</span><span class="title" style="margin-left:40px">Gameplay Rules</span></div>
    <div class="card"><span class="num">01</span><span class="txt">Don't take pictures that reveal puzzle answers or clues.</span></div>
    <div class="card"><span class="num">02</span><span class="txt">Please carry out any special instructions noted after a hole is completed.</span></div>
    <div class="card"><span class="num">03</span><span class="txt">Use props, buttons, knobs, levers or other puzzle elements with care. Don't use force.</span></div>
    <div class="card"><span class="num">04</span><span class="txt">Don't swing putters carelessly. Strokes should not be above knees.</span></div>
    <div class="card"><span class="num">05</span><span class="txt">Don't hit or kick the ball too hard!</span></div>
    <div class="btn bottom">Next</div>
  </div>
</div>
<div class="caption" style="left:471px;top:624px">Gameplay Rules</div>

<div class="phone" style="left:814px;top:78px">
  <div class="notch"></div><div class="status">9:41</div>
  <div class="screen">
    <div class="topbar"><span class="back">←</span><span class="title" style="margin-left:60px">Scoring</span></div>
    <div class="card"><span class="num">01</span><span class="txt">If clues are taken, each player receives points ADDED to their score.<span class="more">Expand +</span></span></div>
    <div class="card"><span class="num">02</span><span class="txt">You can DEDUCT points by earning badges.<span class="more">Expand +</span></span></div>
    <div class="card"><span class="num">03</span><span class="txt">You keep track of individual strokes for each player at each hole.<span class="more">Expand +</span></span></div>
    <div class="card"><span class="num">04</span><span class="txt">Submit scores by pressing this button after each hole.<span class="more">Expand +</span></span></div>
    <div class="btn bottom">Next</div>
  </div>
</div>
<div class="caption" style="left:814px;top:624px">Scoring Rules</div>

<!-- Row 2 -->
<div class="phone" style="left:130px;top:768px">
  <div class="notch"></div><div class="status">9:41</div>
  <div class="screen">
    <div class="topbar"><span class="back">←</span><span class="title" style="margin-left:60px">Badges</span></div>
    <div class="card" style="min-height:44px"><span class="badge-icon"></span><span class="txt">1 point reduction for completing game in under 30 minutes.</span></div>
    <div class="card" style="min-height:44px"><span class="badge-icon"></span><span class="txt">1 point reduction for sharing the team selfie on social media.</span></div>
    <div class="card" style="min-height:44px"><span class="badge-icon"></span><span class="txt">1 point reduction for taking zero clues.</span></div>
    <div class="card" style="min-height:44px"><span class="badge-icon"></span><span class="txt">1 point reduction for taking 1–2 clues entire game.</span></div>
    <div class="card" style="min-height:44px"><span class="badge-icon"></span><span class="txt">1 point reduction for being par or less than par score.</span></div>
    <div class="card" style="min-height:44px"><span class="badge-icon"></span><span class="txt">1 point reduction for hole in one.</span></div>
    <div class="btn bottom">Next</div>
  </div>
</div>
<div class="caption" style="left:130px;top:1314px">Badges Info</div>

<div class="phone" style="left:471px;top:768px">
  <div class="notch"></div><div class="status">9:41</div>
  <div class="screen">
    <div class="topbar"><span class="back">←</span><span class="title" style="margin-left:36px">Important Icons</span></div>
    <div class="note">Icons represent the sequence to be performed at the holes</div>
    <div class="icon-pair" style="margin-top:60px">
      <svg width="26" height="26" viewBox="0 0 26 26"><path d="M20 3 8 19" stroke="var(--pink)" stroke-width="2.5" stroke-linecap="round"/><path d="M5 17h7l-1 5H4z" fill="var(--pink)"/></svg>
      <svg width="26" height="26" viewBox="0 0 26 26" fill="none" stroke="var(--green)" stroke-width="2"><rect x="4" y="7" width="14" height="15" rx="2"/><path d="M18 11h3v6h-3"/></svg>
    </div>
    <div class="note">Put before solving</div>
    <div class="icon-pair" style="margin-top:30px">
      <svg width="26" height="26" viewBox="0 0 26 26" fill="none" stroke="var(--green)" stroke-width="2"><rect x="4" y="7" width="14" height="15" rx="2"/><path d="M18 11h3v6h-3"/></svg>
      <svg width="26" height="26" viewBox="0 0 26 26"><path d="M20 3 8 19" stroke="var(--pink)" stroke-width="2.5" stroke-linecap="round"/><path d="M5 17h7l-1 5H4z" fill="var(--pink)"/></svg>
    </div>
    <div class="note">Solve before putting</div>
    <div class="note" style="margin-top:18px;color:var(--ink)">**NOTE**<br>The order could be different for each hole</div>
    <div class="btn bottom">Next</div>
  </div>
</div>
<div class="caption" style="left:471px;top:1314px">Important Icons</div>

<div class="phone" style="left:814px;top:768px">
  <div class="notch"></div><div class="status">9:41</div>
  <div class="screen">
    <div class="topbar"><span class="back">←</span><span class="title" style="margin-left:56px">Team Info</span></div>
    <div class="input">Enter a Team Name</div>
    <div class="label">Choose the Number of Players</div>
    <div class="count-row"><div class="count on">01</div><div class="count">02</div><div class="count">03</div></div>
    <div class="input">Player 01 Name</div>
    <div class="input">Player 02 Name</div>
    <div class="input">Player 03 Name</div>
    <div class="btn bottom">Continue</div>
  </div>
</div>
<div class="caption" style="left:814px;top:1314px">Team Info</div>

<!-- Row 3 -->
<div class="phone" style="left:130px;top:1457px">
  <div class="notch"></div><div class="status">9:41</div>
  <div class="screen">
    <div class="brand" style="margin-top:6px">Pemberly Under Glass</div>
    <div class="note" style="margin-top:10px;color:var(--ink)">Choose a hole to start playing!</div>
    <div class="hole-grid" style="margin-top:34px">
      <div class="hole">HOLE<span>01</span></div><div class="hole">HOLE<span>02</span></div><div class="hole">HOLE<span>03</span></div>
      <div class="hole">HOLE<span>04</span></div><div class="hole">HOLE<span>05</span></div><div class="hole">HOLE<span>06</span></div>
      <div class="hole">HOLE<span>07</span></div><div class="hole">HOLE<span>08</span></div><div class="hole">HOLE<span>09</span></div>
    </div>
    <div class="brand-small">Burrow Putt</div>
  </div>
</div>
<div class="caption" style="left:130px;top:2003px">Choose a Hole</div>

<div class="phone" style="left:471px;top:1457px">
  <div class="notch"></div><div class="status">9:41</div>
  <div class="screen">
    <div class="brand" style="margin-top:6px">Pemberly Under Glass</div>
    <div class="hole-bar"><span class="chip">HOLE 09</span><span class="chip">PAR 2</span></div>
    <div class="icon-pair">
      <svg width="26" height="26" viewBox="0 0 26 26"><path d="M20 3 8 19" stroke="var(--pink)" stroke-width="2.5" stroke-linecap="round"/><path d="M5 17h7l-1 5H4z" fill="var(--pink)"/></svg>
      <svg width="26" height="26" viewBox="0 0 26 26" fill="none" stroke="var(--green)" stroke-width="2"><rect x="4" y="7" width="14" height="15" rx="2"/><path d="M18 11h3v6h-3"/></svg>
    </div>
    <div class="player" style="margin-top:26px"><div class="name">Owen Marsh</div><div class="slider"><span class="knob-val" style="left:18px">04</span><span class="knob" style="left:20px"></span></div><div class="score">Score: 20</div><div class="current">Current Score</div></div>
    <div class="player"><div class="name">Ned Farley</div><div class="slider"><span class="knob-val" style="left:38px">05</span><span class="knob" style="left:40px"></span></div><div class="score">Score: 24</div><div class="current">Current Score</div></div>
    <div class="player"><div class="name">Ivy Calder</div><div class="slider"><span class="knob-val" style="left:8px">03</span><span class="knob" style="left:10px"></span></div><div class="score">Score: 18</div><div class="current">Current Score</div></div>
    <div class="dock"><span class="square">≡</span><span class="submit">SUBMIT SCORES</span></div>
  </div>
</div>
<div class="caption" style="left:471px;top:2003px">Gameplay</div>

<div class="phone" style="left:814px;top:1457px">
  <div class="notch"></div><div class="status">9:41</div>
  <div class="screen">
    <div class="brand" style="margin-top:6px">Pemberly Under Glass</div>
    <div class="hole-bar"><span class="chip">HOLE 09</span><span class="chip">PAR 2</span></div>
    <div class="icon-pair">
      <svg width="26" height="26" viewBox="0 0 26 26"><path d="M20 3 8 19" stroke="var(--pink)" stroke-width="2.5" stroke-linecap="round"/><path d="M5 17h7l-1 5H4z" fill="var(--pink)"/></svg>
      <svg width="26" height="26" viewBox="0 0 26 26" fill="none" stroke="var(--green)" stroke-width="2"><rect x="4" y="7" width="14" height="15" rx="2"/><path d="M18 11h3v6h-3"/></svg>
    </div>
    <div class="player" style="margin-top:26px"><div class="name">Owen Marsh</div><div class="slider"><span class="knob-val" style="left:18px">04</span><span class="knob" style="left:20px"></span></div><div class="score">Score: 20</div><div class="current">Current Score</div></div>
    <div class="player"><div class="name">Ned Farley</div><div class="slider"><span class="knob-val" style="left:38px">05</span><span class="knob" style="left:40px"></span></div><div class="score">Score: 24</div><div class="current">Current Score</div></div>
    <div class="menu">
      <div class="menu-item"><i></i>Clue Please</div>
      <div class="menu-item"><i></i>Badges</div>
      <div class="menu-item"><i></i>Rules</div>
      <div class="menu-item"><i></i>Take a Selfie</div>
    </div>
    <div class="dock"><span class="square">×</span><span class="submit">SUBMIT SCORES</span></div>
  </div>
</div>
<div class="caption" style="left:814px;top:2003px">Main Menu</div>

<!-- Row 4 -->
<div class="phone" style="left:130px;top:2147px">
  <div class="notch"></div><div class="status">9:41</div>
  <div class="screen">
    <div class="topbar"><span class="back">←</span><span class="title" style="margin-left:40px">Need a Clue?</span></div>
    <div class="note" style="margin-bottom:12px">Once an option is clicked, points are added to your score.</div>
    <div class="clue"><b>Small Nudge!</b><span>1/2 point</span></div>
    <div class="clue"><b>Little Lost!</b><span>1 point</span></div>
    <div class="clue"><b>We Give Up!</b><span>1.5 points</span></div>
    <div class="clue"><b>Nevermind,<br>Don't Need A Clue!</b></div>
  </div>
</div>
<div class="caption" style="left:130px;top:2703px">Clues</div>

<div class="phone" style="left:471px;top:2147px">
  <div class="notch" style="z-index:2"></div>
  <div class="dim"></div>
  <div class="modal">
    <h3>SMALL NUDGE!</h3>
    <div class="note" style="color:var(--ink)">You'll need some rabbit ears to hear parts of a message.</div>
    <div class="btn">Dismiss</div>
  </div>
</div>
<div class="caption" style="left:471px;top:2703px">Viewing a Clue</div>

<div class="phone" style="left:814px;top:2147px">
  <div class="notch"></div><div class="status">9:41</div>
  <div class="screen">
    <div class="topbar"><span class="back">←</span><span class="title">Ready to Submit Scores?</span></div>
    <div class="note">Once confirmed, You can not edit the scores.</div>
    <div class="total"><b>45</b><span>TEAM TOTAL</span></div>
    <div class="btn" style="bottom:60px">Submit Scores</div>
    <div class="btn bottom">Cancel</div>
  </div>
</div>
<div class="caption" style="left:814px;top:2703px">Scorecard</div>

<!-- Row 5 -->
<div class="phone" style="left:130px;top:2831px">
  <div class="notch"></div><div class="status">9:41</div>
  <div class="screen">
    <div class="topbar"><span class="back">←</span><span class="title" style="margin-left:20px">Special Instructions</span></div>
    <div class="note" style="margin-bottom:10px">These instructions are only for Hole 1.</div>
    <div class="card"><span class="num">01</span><span class="txt">Ensure trumpet's chokes are all ground down.</span></div>
    <div class="card"><span class="num">02</span><span class="txt">Move Slider tabs to top row.</span></div>
    <div class="card"><span class="num">03</span><span class="txt">Close door behind you ensuring it's locked.</span></div>
    <div class="btn bottom">Confirm</div>
  </div>
</div>
<div class="caption" style="left:130px;top:3393px">Special Instructions</div>

<div class="phone" style="left:471px;top:2831px">
  <div class="notch"></div><div class="status">9:41</div>
  <div class="screen">
    <div class="topbar"><span class="back">←</span><span class="title" style="margin-left:40px">Take a Selfie</span></div>
    <div class="photo" role="img" aria-label="Live camera preview for the team selfie" style="height:290px;margin:0 -18px"></div>
    <div class="note" style="margin-top:10px">Remember: No Puzzle Solutions in Photos!</div>
    <div class="camera"><span class="cam-small" style="border-radius:50%"></span><span class="shutter"></span><span class="cam-small"></span></div>
  </div>
</div>
<div class="caption" style="left:471px;top:3393px">Take a Selfie</div>

<div class="phone" style="left:814px;top:2831px">
  <div class="notch"></div><div class="status">9:41</div>
  <div class="screen">
    <div class="topbar"><span class="back">←</span><span class="title" style="margin-left:40px">Save or Share</span></div>
    <div class="photo" role="img" aria-label="Captured team selfie preview" style="height:230px"></div>
    <div style="display:flex;justify-content:space-between;align-items:center;padding:6px 4px;border-bottom:1px solid var(--line)"><span class="note">Hunting Fun @</span><span class="brand" style="font-size:9px">Pemberly Under Glass</span></div>
    <div class="btn" style="bottom:60px">Save to Device</div>
    <div class="btn bottom">Share</div>
  </div>
</div>
<div class="caption" style="left:814px;top:3393px">Save or Share</div>

<!-- Row 6 -->
<div class="phone" style="left:471px;top:3524px">
  <div class="notch"></div><div class="status">9:41</div>
  <div class="screen">
    <div class="topbar"><span class="back">←</span><span class="title" style="margin-left:40px">Final Scorecard</span></div>
    <div class="table">
      <table>
        <tr><th></th><th>Player 01</th><th>Player 02</th><th>Player 03</th></tr>
        <tr><td>Strokes</td><td>20</td><td>24</td><td>18</td></tr>
        <tr><td>Clues</td><td>01</td><td>02</td><td>01</td></tr>
        <tr><td>Badges</td><td>03</td><td>02</td><td>03</td></tr>
        <tr><td>Badge Points</td><td>03</td><td>02</td><td>03</td></tr>
        <tr><td>Totals</td><td>18</td><td>24</td><td>16</td></tr>
      </table>
    </div>
    <div class="label" style="margin-top:16px">Top Teams From Last 30 Days</div>
    <div class="team"><span>Team Marlow</span><span>36</span></div>
    <div class="team"><span>Brisk Putters</span><span>41</span></div>
    <div class="btn bottom">Restart</div>
  </div>
</div>
<div class="caption" style="left:471px;top:4080px">Final Scorecard</div>

</body>
</html>
```